Medigap Insurance Interactive website

We are looking at redesigning our website for a more up to date and responsive look and feel. We will code this site using Bootstrap 3 so please research and know how to design for this. Attached is our logo and a wireframe for the new site.
I look forward to seeing what you guys can do.

Target Market(s)

People elegible for Medigap Insurance in the US

Industry/Entity Type

Insurance

Number of Pages Required

5+ page

Font styles to use
Sans Serif

Requirements
Must have
• Match the logo
• Be Bootstrap 3 compatible design
• Font Awesome Icons

```html
<!DOCTYPE html>
<html lang="en">
<head>
<meta charset="utf-8">
<title>Careplan360 – Medicare Supplement</title>
<link rel="stylesheet" href="https://fonts.googleapis.com/css2?family=Open+Sans:wght@400;600;700&family=Cinzel:wght@400&family=Tinos:wght@700&family=Arimo:wght@400&display=swap">
<style>
:root{
  --red:#b21f1a;
  --navy:#0d2a5c;
  --ink:#1a1a1a;
  --grey:#ececec;
  --line:#c9c9c9;
  --muted:#555;
}
*{box-sizing:border-box;margin:0;padding:0}
html,body{width:1200px;height:1188px;overflow:hidden;background:#fff}
body{position:relative;font-family:'Arimo',Arial,sans-serif;color:var(--ink)}
.abs{position:absolute}

/* header */
.brand{left:45px;top:42px;display:flex;align-items:center;gap:8px;font-family:'Open Sans',sans-serif;font-weight:600;font-size:21px;color:var(--ink);line-height:1}
.brand i{width:14px;height:14px;background:var(--navy);display:block}
.nav{left:251px;top:37px;display:flex;height:33px;border:1px solid var(--red);font-family:'Open Sans',sans-serif;font-size:12.5px}
.nav a{display:flex;align-items:center;padding:0 9px;color:var(--ink);text-decoration:none;border-left:1px solid var(--red)}
.nav a:first-child{border-left:0;background:var(--red);color:#fff;font-weight:600;font-size:13px;padding:0 13px}
.callout{left:928px;top:34px;font-family:'Open Sans',sans-serif;text-align:center}
.callout .label{font-size:11.5px;font-weight:700}
.callout .phone{font-size:17px;font-weight:600;margin-top:1px}
.social{left:1099px;top:27px;display:grid;grid-template-columns:24px 24px;gap:4px}
.social span{width:24px;height:24px;display:block}
.s1{background:#d6402f}.s2{background:#3f8fd6}.s3{background:#2f5aa5}.s4{background:#d8483a}

/* hero */
.hero{left:0;top:112px;width:1200px;height:430px}
.why-title{left:420px;top:168px;font-family:'Cinzel',serif;font-size:46px;color:#fff;letter-spacing:2px}
.why-copy{left:412px;top:240px;width:295px;text-align:right;font-family:'Open Sans',sans-serif;font-size:12.6px;line-height:18.5px;color:#fff}
.stat{top:332px;width:110px;text-align:center;color:#fff;font-family:'Open Sans',sans-serif}
.stat .ring{width:80px;height:80px;margin:0 auto;border-radius:50%;background:#fff;display:flex;align-items:center;justify-content:center}
.stat .ring i{width:68px;height:68px;border-radius:50%;border:2px solid var(--navy);display:flex;align-items:center;justify-content:center}
.stat b{display:block;font-size:24px;margin-top:20px;line-height:1}
.stat small{display:block;font-size:12.5px;margin-top:4px}

/* features */
.features{left:0;top:542px;width:1200px;height:226px;background:var(--grey)}
.card{top:580px;width:232px;height:162px;border:1px solid var(--line);text-align:center}
.card .badge{width:102px;height:102px;margin:13px auto 0;border-radius:50%;background:var(--navy);border:5px solid var(--red);display:flex;align-items:center;justify-content:center}
.card h3{font-family:'Open Sans',sans-serif;font-weight:700;font-size:19.5px;letter-spacing:1.2px;margin-top:12px}

/* content */
.divider{top:810px;width:1px;height:240px;background:var(--line)}
.col-title{font-family:'Tinos',serif;font-weight:700;font-size:23.5px;letter-spacing:1.4px;text-align:center}
.about-text{left:48px;top:872px;width:344px;font-size:13.2px;line-height:22.2px;text-align:justify}
.quote{left:435px;top:858px;width:320px;font-size:13.4px;line-height:22.2px}
.avatar{left:437px;top:956px;width:71px;height:79px;border:1px solid var(--line);background:linear-gradient(#e8e8e8,#8a8f98)}
.author{left:518px;top:966px;font-size:13.4px;line-height:19px}
.author .name{color:var(--red)}
.author .role{color:var(--muted)}
.dots{left:523px;top:1010px;display:flex;gap:6px}
.dots span{width:6px;height:6px;background:var(--red)}
.dots span:first-child{background:var(--navy)}
.email{left:798px;top:874px;width:239px;height:36px;border:1px solid var(--line);font-size:13.4px;color:#777;padding:10px 10px}
.signup{left:1050px;top:874px;width:103px;height:36px;background:var(--navy);color:#fff;font-size:16px;display:flex;align-items:center;justify-content:center}
.news-note{left:800px;top:925px;font-size:13.4px}

/* footer */
.footer{left:0;top:1087px;width:1200px;height:101px;background:var(--grey)}
.foot-links{left:0;top:1113px;width:1148px;text-align:center;font-size:13.4px;color:#333}
.foot-links span{padding:0 8px;border-left:1px solid #999}
.foot-links span:first-child{border-left:0}
.foot-rule{left:422px;top:1141px;width:300px;height:1px;background:#999}
.copy{left:0;top:1157px;width:1148px;text-align:center;font-size:13.4px}
</style>
</head>
<body>

<header>
  <div class="abs brand"><i></i>CAREPLAN360</div>
  <nav class="abs nav">
    <a>MEDICARE SUPPLEMENT</a><a>PART D</a><a>HOW TO DECIDE</a><a>LEARN ONLINE</a><a>WHY CAREPLAN360</a><a>BUY NOW</a>
  </nav>
  <div class="abs callout">
    <div class="label">COMPARE RATES AND SAVE</div>
    <div class="phone">(800) 555-0142</div>
  </div>
  <div class="abs social" aria-label="Social links"><span class="s1"></span><span class="s2"></span><span class="s3"></span><span class="s4"></span></div>
</header>

<section class="abs hero">
  <svg width="1200" height="430" viewBox="0 0 1200 430">
    <defs>
      <linearGradient id="globeScene" x1="0" y1="0" x2="1" y2="1">
        <stop offset="0" stop-color="#9fb4c9"/><stop offset=".45" stop-color="#3f77b8"/><stop offset="1" stop-color="#5a4a45"/>
      </linearGradient>
      <linearGradient id="officeScene" x1="0" y1="0" x2="1" y2="1">
        <stop offset="0" stop-color="#dde3ea"/><stop offset=".6" stop-color="#b9b6b3"/><stop offset="1" stop-color="#5b5f66"/>
      </linearGradient>
    </defs>
    <rect x="0" y="0" width="400" height="430" fill="url(#globeScene)" role="img" aria-label="Hand holding a glowing globe with business graphics"/>
    <polygon points="403,0 758,0 758,430 318,430" fill="var(--navy)"/>
    <polygon points="410,0 758,0 758,430 325,430" fill="var(--red)"/>
    <rect x="758" y="0" width="442" height="430" fill="url(#officeScene)" role="img" aria-label="Video still of three colleagues smiling in a meeting"/>
    <circle cx="981" cy="212" r="29" fill="#d8281f"/>
    <polygon points="972,199 972,225 994,212" fill="#fff"/>
    <rect x="758" y="385" width="442" height="45" fill="#262626"/>
    <circle cx="785" cy="407" r="13" fill="#ddd"/>
    <polygon points="781,400 781,414 792,407" fill="#262626"/>
    <rect x="811" y="405" width="308" height="5" fill="#bbb"/>
    <rect x="811" y="405" width="38" height="5" fill="var(--red)"/>
    <polygon points="1131,403 1135,403 1140,399 1140,415 1135,411 1131,411" fill="#ccc"/>
    <path d="M1162 399h5M1162 399v5M1177 399h-5M1177 399v5M1162 415h5M1162 415v-5M1177 415h-5M1177 415v-5" stroke="#ccc" stroke-width="2" fill="none"/>
  </svg>
</section>
<h1 class="abs why-title">WHY US</h1>
<p class="abs why-copy">There are lots of reasons why people needad-vice from a financial adviser but there are also lots of different types of adviser, so it pays to know who to go to and when</p>

<div class="abs stat" style="left:390px">
  <div class="ring"><i><svg width="34" height="34" viewBox="0 0 34 34"><circle cx="13" cy="6" r="4" fill="var(--navy)"/><path d="M8 12h10v10h-3v10h-4V22H8z" fill="var(--navy)"/><circle cx="23" cy="24" r="7" fill="var(--navy)"/><text x="23" y="28" font-size="10" fill="#fff" text-anchor="middle" font-family="Arial">$</text></svg></i></div>
  <b>1170</b><small>Deals</small>
</div>
<div class="abs stat" style="left:492px">
  <div class="ring"><i><svg width="34" height="34" viewBox="0 0 34 34"><circle cx="17" cy="10" r="7" fill="var(--navy)"/><path d="M4 31c0-9 6-12 13-12s13 3 13 12z" fill="var(--navy)"/><path d="M15 19h4l-1 8h-2z" fill="#fff"/></svg></i></div>
  <b>54</b><small>Consultant</small>
</div>
<div class="abs stat" style="left:602px">
  <div class="ring"><i><svg width="36" height="34" viewBox="0 0 36 34"><g fill="none" stroke="var(--navy)" stroke-width="2.5"><ellipse cx="18" cy="8" rx="10" ry="5"/><path d="M8 14c0 3 4 5 10 5s10-2 10-5M8 20c0 3 4 5 10 5s10-2 10-5M8 26c0 3 4 5 10 5s10-2 10-5"/></g></svg></i></div>
  <b>995</b><small>Happy Customer</small>
</div>

<section class="abs features"></section>
<div class="abs card" style="left:45px">
  <div class="badge"><svg width="52" height="52" viewBox="0 0 52 52"><g fill="none" stroke="#fff" stroke-width="3.5"><path d="M10 22a17 17 0 0 1 30-8"/><path d="M42 30a17 17 0 0 1-30 8"/><circle cx="26" cy="26" r="10"/></g><path d="M40 6v10h-10z" fill="#fff"/><path d="M12 46V36h10z" fill="#fff"/><text x="26" y="31" font-size="14" font-weight="700" fill="#fff" text-anchor="middle" font-family="Arial">$</text></svg></div>
  <h3>Compare Rates</h3>
</div>
<div class="abs card" style="left:337px">
  <div class="badge"><svg width="50" height="50" viewBox="0 0 50 50"><path d="M4 10h8l6 22h22l5-16" fill="none" stroke="#fff" stroke-width="4" stroke-linejoin="round"/><circle cx="20" cy="41" r="4" fill="#fff"/><circle cx="37" cy="41" r="4" fill="#fff"/><path d="M29 4v14M23 13l6 7 6-7" fill="none" stroke="#fff" stroke-width="4"/></svg></div>
  <h3>Buy Now</h3>
</div>
<div class="abs card" style="left:627px">
  <div class="badge"><svg width="44" height="50" viewBox="0 0 44 50"><circle cx="22" cy="10" r="8" fill="#fff"/><path d="M8 30c0-8 6-11 14-11s14 3 14 11z" fill="#fff"/><path d="M4 30l18 6 18-6v14l-18 6-18-6z" fill="#fff"/><path d="M22 36v14" stroke="var(--navy)" stroke-width="2"/></svg></div>
  <h3>Learn Online</h3>
</div>
<div class="abs card" style="left:918px">
  <div class="badge"><svg width="40" height="56" viewBox="0 0 40 56"><path d="M7 16a13 13 0 1 1 20 11c-5 3-6 5-6 11" fill="none" stroke="#fff" stroke-width="7"/><rect x="17" y="44" width="8" height="8" fill="#fff"/></svg></div>
  <h3>Get Expert Help</h3>
</div>

<div class="abs divider" style="left:409px"></div>
<div class="abs divider" style="left:770px"></div>

<h2 class="abs col-title" style="left:48px;top:817px;width:344px">About us</h2>
<p class="abs about-text">Don eclacu s nibh, vulputate eu diam non, sodales tincidunt ligula.Pellente sque molestie nisl i n dolor gravida commod-Lor em ipsum dolor sit amet, co nsectetur adipiscing elit. Done clac us nibh, vulputate eu dianon, sodales tincid unt ligul a.Pelle ntesque mol nisl in dolor gravida commodo.-Donecla cu s nibh, vulputate eu diam non, sodales tincidunt lig ula.Pell ente sque molestie nisl iscing elit. Doneclac us</p>

<h2 class="abs col-title" style="left:420px;top:815px;width:340px">What people are saying</h2>
<p class="abs quote">Lorem ipsum dolor sit amet, consectetur adipiscing elit. Doneclacus nibh, vulputate eu diam non, sodales tincid unt ligula.Pellentesque molestie nisl in dolor gravida commodo.</p>
<div class="abs avatar" role="img" aria-label="Portrait of the quoted client"></div>
<div class="abs author"><div class="name">Dorin Veltan</div><div class="role">CEO Northway Group</div></div>
<div class="abs dots"><span></span><span></span><span></span><span></span></div>

<h2 class="abs col-title" style="left:790px;top:817px;width:375px">Get Monthly Update</h2>
<div class="abs email">Email Address</div>
<div class="abs signup">Sign Up</div>
<p class="abs news-note">Enter email for customized rate updates and more</p>

<footer class="abs footer"></footer>
<div class="abs foot-links"><span>Careplan360</span><span>Sitemap</span><span>Buy Now</span><span>Blog</span><span>Login</span></div>
<div class="abs foot-rule"></div>
<div class="abs copy">© 2016 Careplan360&nbsp; All Right Reserved.</div>

</body>
</html>
```